I need package design designs for an organic, natural, unrefined shea butter packaged in a pouch like the example below. The package design should express pure, organic, freshness, moisturizing and healthy. The package design should also reflect the benefits of the product listed below. The product will be called “ORGANIC SHEA BUTTER”
MEANING OF NAME: KERO AFRICA" meaning to Come to Africa for your natural cosmetics
Logo Text/Brand Name:
“KERO”
Logo Styles of Interest:
Elegance
Natural
Organic
Freshness
Unrefined
From a tree nut
Target Market:
General public
Must have:
KISS : Keep it simple stupid
Note: I have a shea nuts stock photo i can provide.
Dimension:W = 7.48 InchesH = 10.43 inches Added Thursday, January 14, 2016
Cosmetics

```html
<!DOCTYPE html>
<html lang="en">
<head>
<meta charset="utf-8">
<title>KERO Organic Shea Butter Pouch</title>
<link rel="stylesheet" href="https://fonts.googleapis.com/css2?family=Montserrat:wght@500;600;800;900&display=swap">
<style>
  :root {
    --stage: #d9dadb;
    --navy: #1f4a68;
    --navy-deep: #163a55;
    --white: #ffffff;
    --kraft: #c99460;
    --kraft-dark: #b77f4b;
    --mint: #93d4bb;
    --mint-ink: #ffffff;
    --ink: #1c1a18;
    --badge: #17364f;
    --bean-dark: #2a1a14;
    --bean-mid: #4a2c20;
    --leaf: #4e6e4a;
  }
  * { box-sizing: border-box; margin: 0; padding: 0; }
  html, body {
    width: 1200px; height: 1200px; overflow: hidden;
    background: var(--stage);
    font-family: "Montserrat", Arial, sans-serif;
  }
  .pouch-face {
    position: absolute; left: 280px; top: 70px;
    width: 640px; height: 1060px;
    background: linear-gradient(180deg, var(--navy) 0%, var(--navy-deep) 55%);
    overflow: hidden;
  }
  .nut-photo {
    position: absolute; left: 0; top: 560px; width: 640px; height: 500px;
    background:
      radial-gradient(ellipse 160px 120px at 110px 170px, var(--leaf) 0%, transparent 70%),
      radial-gradient(ellipse 300px 220px at 420px 360px, var(--bean-mid) 0%, transparent 75%),
      linear-gradient(180deg, #3a2419 0%, var(--bean-dark) 100%);
  }
  .brand-name {
    position: absolute; top: 150px; left: 0; width: 100%;
    text-align: center; color: var(--white);
    font-weight: 900; font-size: 112px; letter-spacing: 2px; line-height: 1;
  }
  .badge {
    position: absolute; left: 248px; top: 318px;
    width: 144px; height: 144px; border-radius: 50%;
    background: var(--badge);
    border: 3px solid var(--mint);
    z-index: 3;
  }
  .tag {
    position: absolute; left: 40px; top: 478px;
    width: 560px; height: 290px;
    transform: rotate(10deg); transform-origin: center;
    background: linear-gradient(135deg, var(--kraft) 0%, var(--kraft-dark) 100%);
    clip-path: polygon(12% 0, 100% 0, 100% 100%, 12% 100%, 0 72%, 0 28%);
    z-index: 2;
  }
  .tag-hole {
    position: absolute; left: 22px; top: 133px;
    width: 22px; height: 22px; border-radius: 50%;
    background: var(--navy-deep);
  }
  .claim-pill {
    position: absolute; left: 130px; top: 52px;
    width: 310px; height: 62px; border-radius: 16px;
    background: var(--mint); color: var(--mint-ink);
    font-weight: 600; font-size: 34px; white-space: nowrap;
    display: flex; align-items: center; justify-content: center;
  }
  .product-name {
    position: absolute; left: 56px; right: 16px; top: 140px;
    text-align: center;
    color: var(--ink); font-weight: 600; font-size: 36px; letter-spacing: 0;
    white-space: nowrap; line-height: 1;
  }
  .origin {
    position: absolute; left: 56px; right: 16px; top: 198px;
    text-align: center;
    color: var(--ink); font-weight: 600; font-size: 17px;
  }
  .net-weight {
    position: absolute; top: 878px; left: 0; width: 100%;
    text-align: center; color: var(--white); font-weight: 600; font-size: 19px;
  }
  .divider {
    position: absolute; top: 936px; left: 160px; width: 320px; height: 2px;
    background: var(--white);
  }
  .usage-note {
    position: absolute; top: 966px; left: 0; width: 100%;
    text-align: center; color: var(--white); font-weight: 500; font-size: 15px;
  }
</style>
</head>
<body>
  <main class="pouch-face">
    <div class="nut-photo" role="img" aria-label="Photo of shea nuts with green leaves"></div>
    <h1 class="brand-name">KERO</h1>
    <div class="badge" aria-hidden="true"></div>
    <div class="tag">
      <span class="tag-hole"></span>
      <div class="claim-pill">100% NATURAL</div>
      <div class="product-name">ORGANIC SHEA BUTTER</div>
      <div class="origin">Produced in Ghana</div>
    </div>
    <div class="net-weight">16 OZ.</div>
    <div class="divider"></div>
    <div class="usage-note">External Use Only</div>
  </main>
</body>
</html>
```